Sun-Pod Coffee Kiosks Webdesign project

Sun-Pod Coffee Kiosks provides coffee carts, kiosks, and/or drive thrus depending on location. At Sun-Pod our company focuses on offering healthy snack & drink options for people on the go as well as nutritional coaching with our daily "Pod notes." We will provide some healthy snacks as well.

We offer all organic coffee & espresso drinks,100% real fruit & vegetable smoothies, protein shakes, and healthy breakfast/snack items.

I want "balance" to be a big theme in the website design. True well-being is a balance of body (health), mind (emotional well-being) and spirit (we are a Christian based company who loves and accepts all people, sexual orientation, religions, ect)

My parents are missionaries and founded the Nicaraguan organization "Bright Path Outreach Nicaragua" over 11 years ago ( www.brightpathoutreach.org ). Sun-Pod plans to be a financial partner to their mission so 10% of profits or 2% of total revenue, whichever is greater will go to Bright Path and their church plants & medical/dental clinic. I want this and info about Bright Path to have a page on the website.

Target Market(s)

Ages 18-54 (target coffee customer).

Industry/Entity Type

Financial

Requirements
Must have
• -Home page
-Menu page
-Locations page/contact page
-Kiosk options page (cart, kiosk & drive thru descriptions, pics, traffic & location needs, ect)
-Fundraising/Bright Path Outreach Nicaragua page
Nice to have
• I have a logo designed that I attached. I would like the colors to be dark brown, light brown, and a lime green. My business card is also attached.

```html
<!DOCTYPE html>
<html lang="en">
<head>
<meta charset="utf-8">
<title>Sun-Pod Organic Coffee</title>
<link rel="stylesheet" href="https://fonts.googleapis.com/css2?family=Montserrat:wght@400;500;700;800&display=swap">
<style>
  :root {
    --lime: #a9d46a;
    --lime-light: #bde08a;
    --brown-dark: #3b2414;
    --brown-deep: #412816;
    --brown-mid: #6b3422;
    --tan: #b88a5a;
    --tan-mid: #c9a266;
    --sand: #e6d39a;
    --cream: #f1e2b0;
    --text-dark: #3a2412;
  }
  * { margin: 0; padding: 0; box-sizing: border-box; }
  html, body { width: 1200px; height: 827px; overflow: hidden; }
  body { font-family: "Montserrat", sans-serif; background: var(--brown-deep); position: relative; }

  .hero-band {
    position: absolute; left: 0; top: 0; width: 1200px; height: 582px;
    background: radial-gradient(ellipse at 50% 40%, var(--lime-light) 0%, var(--lime) 70%, #9ccb5c 100%);
  }
  .brand { position: absolute; left: 198px; top: 22px; width: 190px; text-align: center; }
  .brand-dot { width: 48px; height: 48px; border-radius: 50%; background: var(--brown-mid); margin: 0 auto 8px; }
  .brand-name { font-size: 38px; font-weight: 700; color: var(--text-dark); letter-spacing: -1.5px; line-height: 1; white-space: nowrap; }
  .brand-tag { font-size: 9px; color: var(--brown-mid); letter-spacing: 2px; margin-top: 10px; white-space: nowrap; }

  .contact { position: absolute; left: 496px; top: 34px; display: flex; align-items: center; white-space: nowrap; }
  .contact-note { color: #fff; font-size: 11.5px; font-weight: 500; margin-right: 14px; }
  .contact-phone { color: #fff; font-size: 30px; font-weight: 800; letter-spacing: -0.5px; margin-left: 6px;
    text-shadow: 0 1px 1px rgba(0,0,0,0.25); }

  .main-nav { position: absolute; left: 458px; top: 86px; width: 742px; height: 47px; background: var(--brown-dark);
    box-shadow: 0 8px 10px rgba(0,0,0,0.25); display: flex; align-items: center; padding-left: 20px; }
  .main-nav a { color: #fff; text-decoration: none; font-size: 12px; font-weight: 500; padding: 0 21px; line-height: 16px;
    border-right: 1px dashed rgba(255,255,255,0.35); display: flex; align-items: center; white-space: nowrap; }
  .main-nav a:last-child { border-right: none; }
  .main-nav .caret { margin-left: 6px; }

  .hero-visual { position: absolute; left: 250px; top: 184px; width: 716px; height: 290px; border-radius: 22px;
    background: linear-gradient(90deg, #e7c38c 0%, #f3ead8 35%, #c08a55 58%, #f1e7cf 72%, #e2d2a6 82%, #6b4a2c 100%);
    box-shadow: 0 10px 18px rgba(60,90,20,0.25); }
  .slider-arrow { position: absolute; top: 278px; }
  .slider-arrow.prev { left: 54px; }
  .slider-arrow.next { left: 1045px; }

  .hero-title { position: absolute; left: 222px; top: 498px; font-size: 31px; font-weight: 800; color: var(--text-dark);
    letter-spacing: -1.6px; white-space: nowrap; line-height: 36px; }
  .hero-sub { position: absolute; left: 222px; top: 536px; font-size: 11.5px; color: var(--text-dark); font-weight: 500; white-space: nowrap; }
  .hero-button { position: absolute; left: 722px; top: 501px; width: 240px; height: 50px;
    background: linear-gradient(#6e3522, #5a2a1a); box-shadow: 0 3px 3px rgba(0,0,0,0.3);
    color: #fff; font-size: 26px; font-weight: 800; letter-spacing: -1.5px; display: flex; align-items: center; justify-content: center; white-space: nowrap; }

  .welcome { position: absolute; left: 222px; top: 604px; display: flex; align-items: center; }
  .welcome-title { font-size: 25px; font-weight: 800; color: var(--cream); letter-spacing: -1.2px; padding-right: 14px;
    border-right: 1px solid rgba(241,226,176,0.4); height: 26px; line-height: 26px; }
  .welcome-text { font-size: 11.3px; color: var(--cream); line-height: 17px; padding-left: 18px; width: 600px; }

  .features { position: absolute; left: 230px; top: 670px; display: flex; gap: 5px; }
  .feature { width: 240px; height: 91px; display: flex; align-items: center; padding-left: 8px; }
  .feature.notes { background: var(--tan); }
  .feature.menu { background: var(--tan-mid); }
  .feature.location { background: var(--sand); }
  .feature-icon { width: 60px; display: flex; justify-content: center; }
  .feature-title { font-size: 22px; font-weight: 800; color: var(--text-dark); letter-spacing: -1.2px; line-height: 1; white-space: nowrap; }
  .feature-text { font-size: 10.5px; color: var(--text-dark); line-height: 14px; margin-top: 5px; }

  .footer-links { position: absolute; left: 231px; top: 793px; font-size: 9.5px; color: var(--cream); white-space: nowrap; }
  .social { position: absolute; left: 588px; top: 792px; display: flex; gap: 4px; }
  .social span { width: 12px; height: 12px; border-radius: 2px; background: #a6cf62; display: block; }
  .copyright { position: absolute; right: 238px; top: 793px; font-size: 9.5px; color: #8f6a3f; white-space: nowrap; }
</style>
</head>
<body>
  <section class="hero-band">
    <div class="brand">
      <div class="brand-dot"></div>
      <div class="brand-name">Sun-Pod</div>
      <div class="brand-tag">ORGANIC COFFEE</div>
    </div>

    <div class="contact">
      <span class="contact-note">Call About Catering - Coffee Delivering</span>
      <svg width="16" height="20" viewBox="0 0 16 20"><path d="M4 1 L7 5 L5 8 Q7 12 10 14 L13 12 L15 16 L12 19 Q2 14 1 4 Z" fill="#6b3422"/></svg>
      <span class="contact-phone">919-555-0142</span>
    </div>

    <nav class="main-nav">
      <a href="#">HOME</a>
      <a href="#">MENU</a>
      <a href="#">LOCATIONS</a>
      <a href="#">KIOSK <svg class="caret" width="9" height="6" viewBox="0 0 9 6"><path d="M1 1 L4.5 5 L8 1" stroke="#8a3a26" stroke-width="2" fill="none"/></svg></a>
      <a href="#">FUNDRAISING</a>
    </nav>

    <div class="hero-visual" role="img" aria-label="Breakfast plate with hash browns, breaded steak with gravy and fried eggs, a smoothie glass with apple slice and a Sun-Pod coffee cup"></div>

    <svg class="slider-arrow prev" width="58" height="118" viewBox="0 0 58 118"><path d="M57 1 L1 59 L57 117" stroke="rgba(255,255,255,0.55)" stroke-width="1.2" fill="none"/></svg>
    <svg class="slider-arrow next" width="58" height="118" viewBox="0 0 58 118"><path d="M1 1 L57 59 L1 117" stroke="rgba(255,255,255,0.55)" stroke-width="1.2" fill="none"/></svg>

    <h1 class="hero-title">HEALTHY BITES, ON THE GO!</h1>
    <p class="hero-sub">Organic Coffee Espressp &amp; Tea , Blendwell Smoothies &amp; Protein Shakes and more...</p>
    <div class="hero-button">MORE DETAILS</div>
  </section>

  <section class="welcome">
    <h2 class="welcome-title">WELCOME</h2>
    <p class="welcome-text">Sun-Pod plans to be a financial partner to their mission so 10% of profits or 2% of total revenue, whichever is greater will go to Bright Path and their church plants &amp; medical/dental clinic.</p>
  </section>

  <section class="features">
    <div class="feature notes">
      <div class="feature-icon"><svg width="48" height="48"><circle cx="24" cy="24" r="23" fill="#4a2614"/></svg></div>
      <div><div class="feature-title">POD NOTES</div><div class="feature-text">Lorem ipsum dolor sit amet,<br>consectetuer adipiscing...</div></div>
    </div>
    <div class="feature menu">
      <div class="feature-icon"><svg width="48" height="48"><circle cx="24" cy="24" r="23" fill="#4a2614"/></svg></div>
      <div><div class="feature-title">OUR MENU</div><div class="feature-text">Lorem ipsum dolor sit amet,<br>consectetuer adipiscing...</div></div>
    </div>
    <div class="feature location">
      <div class="feature-icon"><svg width="44" height="70" viewBox="0 0 44 70"><path d="M22 69 L5 36 A20 20 0 1 1 39 36 Z" fill="#3b2414"/><circle cx="22" cy="21" r="7" fill="#e6d39a"/></svg></div>
      <div><div class="feature-title">LOCATION</div><div class="feature-text">Lorem ipsum dolor sit amet,<br>consectetuer adipiscing...</div></div>
    </div>
  </section>

  <footer>
    <div class="footer-links">HOME - MENU - LOCATIONS - KIOSK - FUNDRAISING</div>
    <div class="social"><span></span><span></span><span></span><span></span></div>
    <div class="copyright">Copyright © 2013 Sun-Pod.&nbsp; All rights reserved.</div>
  </footer>
</body>
</html>
```